lumavista web design

- Company / Site Description
We are developing a website that will allow anyone in Europe to find in one click, cultural things to do (Exhibition, Museum, Monument, Zoo, Aquarium, Archaeological site…) with friends or family, and to organize the visit (book a ticket / a private visit, book a restaurant nearby…).

Examples
1. You're in London with your girlfriend, it's saturday 10 am, you have two hours to spend and you want to see an exhibition. We provide you in one click all the exhibition matching your location / time and date.

2. You're in Berlin with some friends, it's thursday night you want to go out, but you don't know what to do. We provide you a list of experience, you can select for instance "I want to be on top of the world", and we show you a list of venues matching the selected experience / date / time /location of your request.

- Brand name : Lumavista
- Activity : Cultural Leisure, cultural entertainment

- Target audience
Broad target will be between 20 and 55. Core target will be between 25 and 40. Most likely to live in a city and in Europe.

- Behaviours and preferences
Our user is under time constraint (few minutes to find and choose his visit), idea constraint (is not sure about what to do and see) and money constraint.
He wants to have an easy to use website, not cluttered with information, focussed on added value information. He wants to have a website which is modern, fun and elegant that he will deem as professional and trustworthy.

- Our expectations (Do’s and Don’t)
We want to move away from traditional design. We want some OUT OF THE BOX design. Think of a website design that will look like an app design.
We want to make an awesome / extra ordinary /remember-able design. The design must be so cool, that the user wants to come back to the site. In two words: THINK EXTRAORDINARY.
You can use photos to help the user understand functions. If you use photo, use creative commons license photo.
Avoid black colors

- Functional Requirements
We need Four pages:
1. Home Page (desktop and mobile version): it’s both the homepage and the assistant page. This page will allow the user to find in one click his visit (please refer to the pdf file Assistant home page). The page must be self-explanatory for a first time user.
2. Assistant result page (desktop version): it’s the page that display the results found by the assistant based on the criteria search (please refer to the pdf file mockup - Assistant result page)
3. Site / Event page (desktop version): it’s the page that display each result information (please refer to the pdf file mockup – Event / Site Page)
The pdf files list all the elements include in each page + gives you a mockup of each page (just to put in perspective the element required). You are completely free about the design.
We don’t have the logo yet. Use a dummy logo for your page design.
The selected winner can expect to work with us immediately after the contest and on a on a regular basis later on.

- Technical Requirements
No Flash
For the winner, we will manage the CSS you will just need to provide :
. One PSD file containing all the pages
. Inside the PSD file we want for each page two groups: the first group will embed the desktop design, the second group will embed the responsive mobile design (Home Page only).
In total there should be 4 groups inside the PSD file (3 desktop groups, 1 mobile group).
Each group must contain all the elements specified in the pdf file

Website we like
http://demo.pallorthemes.example/?theme=Vuntel
http://rosetta.quilbershop.example/#home
http://blogsite.trask.moveldock.example/2/
http://demo.pallorthemes.example/?theme=Obelune
http://www.gravonix.example/themes/tallow/
http://skinmarket.example/item/kelp-responsive-photography-blog-theme/full_screen_preview/8817206
http://products.qdvworks.example/?product=example
http://uk.tavershaw.example

Reason: Due to the request of several designers, we have agreed to add 7 additional days to the contest deadline. Thank you. The lumavista team

Reason: We still need to collect all the votes. Sorry for the delay.

Reason: Hello, We extend the contest deadline, in order to collect all the votes from the poll. We should have everything finalized by sunday. Thank you lumavista team

```html
<!DOCTYPE html>
<html lang="en">
<head>
<meta charset="utf-8">
<title>Lumavista – Find your visit in one click</title>
<link href="https://fonts.googleapis.com/css2?family=PT+Sans:wght@400;700&display=swap" rel="stylesheet">
<style>
  :root {
    --accent: #f25749;
    --page-bg: #f3f1f2;
    --white: #ffffff;
    --line: #dedcdd;
    --text-strong: #6d6b6c;
    --text-mid: #8a8889;
    --text-soft: #a9a7a8;
    --weather-bg: #e8e6e7;
    --go-bg: #efedee;
    --icon-grey: #a5a3a4;
  }
  * { box-sizing: border-box; margin: 0; padding: 0; }
  html, body { width: 1200px; height: 1000px; overflow: hidden; }
  body {
    position: relative;
    background: var(--page-bg);
    font-family: "PT Sans", Arial, sans-serif;
    color: var(--text-mid);
  }

  /* Header */
  .site-header { position: absolute; left: 0; top: 0; width: 1200px; height: 115px; background: var(--white); }
  .brand { position: absolute; left: 134px; top: 52px; font-size: 37px; font-weight: 400; letter-spacing: 0.5px; color: var(--text-mid); line-height: 1; }
  .social { position: absolute; left: 984px; top: 63px; display: flex; gap: 5px; }
  .social span { width: 21px; height: 21px; background: var(--icon-grey); display: block; }
  .social .more { position: relative; }
  .social .more::before, .social .more::after { content: ""; position: absolute; background: var(--white); }
  .social .more::before { left: 5px; top: 9px; width: 11px; height: 3px; }
  .social .more::after { left: 9px; top: 5px; width: 3px; height: 11px; }

  /* Navigation */
  .main-nav { position: absolute; left: 0; top: 115px; width: 1200px; height: 44px; border-bottom: 1px solid var(--line); background: var(--page-bg); }
  .nav-link { position: absolute; top: 13px; font-size: 15px; color: var(--text-strong); }
  .nav-link.active { color: var(--accent); }
  .nav-assistant { left: 135px; }
  .nav-favourites { left: 266px; }
  .search { position: absolute; left: 814px; top: 0; width: 171px; height: 43px; border-left: 1px solid var(--line); border-right: 1px solid var(--line); }
  .search-label { position: absolute; left: 13px; top: 15px; font-size: 11px; color: var(--text-soft); }
  .search svg { position: absolute; left: 951px; }
  .search-icon { position: absolute; left: 138px; top: 12px; }
  .login { position: absolute; left: 985px; top: 0; width: 101px; height: 43px; border-right: 1px solid var(--line); }
  .login-label { position: absolute; left: 31px; top: 15px; font-size: 11px; color: var(--text-soft); letter-spacing: 0.3px; }
  .login svg { position: absolute; left: 75px; top: 18px; }

  /* Intro */
  .intro { position: absolute; left: 0; top: 224px; width: 1200px; text-align: center; }
  .intro-title { font-size: 28px; font-weight: 400; color: var(--text-strong); }
  .intro-title em { font-style: normal; color: var(--accent); }
  .intro-sub { margin-top: 9px; font-size: 19px; color: var(--text-mid); }

  /* Cards */
  .card { position: absolute; background: var(--white); }
  .card-image { width: 100%; height: 199px; display: block; }
  .card-title { position: absolute; left: 18px; top: 219px; font-size: 11px; font-weight: 700; color: var(--text-mid); letter-spacing: 0.2px; }
  .card-tags { position: absolute; left: 18px; top: 244px; font-size: 9px; color: var(--text-soft); letter-spacing: 0.2px; }
  .card-tags b { font-size: 10px; color: var(--text-mid); margin-right: 8px; }
  .card-menu { position: absolute; right: 17px; top: 229px; }
  .card-a { left: 136px; top: 360px; width: 340px; height: 280px; }
  .card-b { left: 489px; top: 360px; width: 287px; height: 280px; }
  .card-c { left: 136px; top: 666px; width: 340px; height: 279px; }
  .card-d { left: 489px; top: 666px; width: 287px; height: 279px; }
  .img-animals { background: linear-gradient(160deg, #3c4a28 0%, #b07a3c 40%, #e8e2d6 70%, #5f7a35 100%); }
  .img-museum { background: linear-gradient(180deg, #5b7fc4 0%, #b9c9ea 35%, #f2f4fb 60%, #c7ccd8 100%); }
  .img-place { background: linear-gradient(180deg, #3b3a22 0%, #6f6a3a 35%, #4a3a2a 70%, #2e2620 100%); }

  /* Sidebar */
  .assistant-panel { position: absolute; left: 805px; top: 360px; width: 280px; height: 412px; background: var(--white); }
  .weather { position: absolute; left: 17px; top: 15px; width: 247px; height: 184px; background: var(--weather-bg); border-radius: 10px; }
  .weather-label { position: absolute; left: 23px; top: 23px; font-size: 11px; font-weight: 700; color: var(--text-soft); }
  .weather-temp { position: absolute; left: 23px; top: 40px; display: flex; align-items: center; gap: 9px; font-size: 24px; color: var(--text-soft); }
  .weather-rule { position: absolute; left: 22px; top: 77px; width: 196px; height: 1px; background: #d8d6d7; }
  .weather-line { position: absolute; left: 22px; font-size: 12px; color: var(--text-mid); letter-spacing: 0.3px; }
  .weather-date { top: 96px; }
  .weather-time { top: 123px; }
  .weather-place { top: 150px; }
  .weather-place b { font-weight: 700; }
  .want-button { position: absolute; left: 17px; top: 229px; width: 245px; height: 49px; background: var(--accent); color: var(--white); font-size: 14px; font-weight: 700; text-align: center; line-height: 50px; }
  .go-button { position: absolute; left: 102px; top: 299px; width: 82px; height: 77px; border-radius: 50%; background: var(--go-bg); color: #cfcdce; font-size: 17px; font-weight: 700; text-align: center; line-height: 77px; }

  /* Footer */
  .site-footer { position: absolute; left: 0; top: 965px; width: 1200px; height: 35px; background: var(--accent); color: var(--white); font-size: 12px; font-weight: 700; }
  .language { position: absolute; left: 135px; top: 12px; }
  .more-link { position: absolute; left: 1026px; top: 13px; display: flex; align-items: center; gap: 13px; }
</style>
</head>
<body>

<header class="site-header">
  <div class="brand">LUMAVISTA</div>
  <div class="social" aria-label="Social links">
    <span></span><span></span><span></span><span class="more"></span>
  </div>
</header>

<nav class="main-nav">
  <span class="nav-link nav-assistant active">MyAssistant</span>
  <span class="nav-link nav-favourites">MyFavourites</span>
  <div class="search">
    <span class="search-label">Search</span>
    <svg class="search-icon" width="18" height="18" viewBox="0 0 18 18" fill="none" stroke="#a5a3a4" stroke-width="1.6">
      <circle cx="7" cy="7" r="5.5"/><line x1="11" y1="11" x2="16.5" y2="16.5" stroke-width="2.4"/>
    </svg>
  </div>
  <div class="login">
    <span class="login-label">LOGIN</span>
    <svg width="9" height="6" viewBox="0 0 9 6" fill="none" stroke="#b5b3b4" stroke-width="1.4"><polyline points="1,1 4.5,4.5 8,1"/></svg>
  </div>
</nav>

<section class="intro">
  <h1 class="intro-title">Find in <em>one click</em> Exhibitions, museums, monuments, zoos…</h1>
  <p class="intro-sub">Tell us what you like, we will tell you where to go!</p>
</section>

<article class="card card-a">
  <div class="card-image img-animals" role="img" aria-label="Photo of two tigers lying on grass"></div>
  <div class="card-title">WILD ANIMALS</div>
  <div class="card-tags"><b>TAG:</b>LION &nbsp;| MONKEY | TIGER</div>
  <svg class="card-menu" width="17" height="16" viewBox="0 0 17 16" fill="#c9c7c8"><rect y="0" width="17" height="2.5"/><rect y="4.5" width="17" height="2.5"/><rect y="9" width="17" height="2.5"/><rect y="13.5" width="17" height="2.5"/></svg>
</article>

<article class="card card-b">
  <div class="card-image img-museum" role="img" aria-label="Photo of a museum great court under a glass roof"></div>
  <div class="card-title">MUSEUM</div>
  <div class="card-tags"><b>TAG:</b>BRITISH &nbsp;| EN | EXAMPLE</div>
  <svg class="card-menu" width="17" height="16" viewBox="0 0 17 16" fill="#c9c7c8"><rect y="0" width="17" height="2.5"/><rect y="4.5" width="17" height="2.5"/><rect y="9" width="17" height="2.5"/><rect y="13.5" width="17" height="2.5"/></svg>
</article>

<article class="card card-c">
  <div class="card-image img-place" role="img" aria-label="Photo of a gothic cathedral interior"></div>
  <div class="card-title">PLACE</div>
  <div class="card-tags"><b>TAG:</b>NEW YORK &nbsp;| AUSTRALIA | BRAZIL</div>
  <svg class="card-menu" width="17" height="16" viewBox="0 0 17 16" fill="#c9c7c8"><rect y="0" width="17" height="2.5"/><rect y="4.5" width="17" height="2.5"/><rect y="9" width="17" height="2.5"/><rect y="13.5" width="17" height="2.5"/></svg>
</article>

<article class="card card-d">
  <div class="card-image img-museum" role="img" aria-label="Photo of a museum great court under a glass roof"></div>
  <div class="card-title">MUSEUM</div>
  <div class="card-tags"><b>TAG:</b>BRITISH &nbsp;| EN | EXAMPLE</div>
  <svg class="card-menu" width="17" height="16" viewBox="0 0 17 16" fill="#c9c7c8"><rect y="0" width="17" height="2.5"/><rect y="4.5" width="17" height="2.5"/><rect y="9" width="17" height="2.5"/><rect y="13.5" width="17" height="2.5"/></svg>
</article>

<aside class="assistant-panel">
  <div class="weather">
    <div class="weather-label">WEATHER</div>
    <div class="weather-temp">
      <svg width="30" height="30" viewBox="0 0 30 30" fill="none" stroke="#b9b7b8" stroke-width="1.5">
        <circle cx="15" cy="15" r="6" fill="#b9b7b8"/>
        <g stroke-linecap="round">
          <line x1="15" y1="1" x2="15" y2="6"/><line x1="15" y1="24" x2="15" y2="29"/>
          <line x1="1" y1="15" x2="6" y2="15"/><line x1="24" y1="15" x2="29" y2="15"/>
          <line x1="5" y1="5" x2="8.5" y2="8.5"/><line x1="21.5" y1="21.5" x2="25" y2="25"/>
          <line x1="25" y1="5" x2="21.5" y2="8.5"/><line x1="8.5" y1="21.5" x2="5" y2="25"/>
        </g>
      </svg>
      <span>16˚ c</span>
    </div>
    <div class="weather-rule"></div>
    <div class="weather-line weather-date">THURSDAY, 27 FEBRUARY 2014</div>
    <div class="weather-line weather-time">11.00 am</div>
    <div class="weather-line weather-place">PARIS, <b>FRANCE</b></div>
  </div>
  <div class="want-button">YOU WANT ?</div>
  <div class="go-button">GO</div>
</aside>

<footer class="site-footer">
  <span class="language">Language : English</span>
  <span class="more-link">PLUS
    <svg width="17" height="17" viewBox="0 0 17 17"><circle cx="8.5" cy="8.5" r="8.5" fill="#fff"/><polygon points="4.5,6.5 12.5,6.5 8.5,11" fill="#f25749"/></svg>
  </span>
</footer>

</body>
</html>
```